Business Card Design

My business is writing crime novels to entertain readers. I write legal thrillers and mysteries. I need a card for publishers, agents, other authors, and media.

Industry/Entity Type

Legal

Contact Information for Business Card

Paul Ostrander
www.ostranderthrillers.example
paulbostrander@mailbox.example
0064 27 5139427

```html
<!DOCTYPE html>
<html lang="en">
<head>
<meta charset="utf-8">
<title>Paul Ostrander — Business Card</title>
<link rel="stylesheet" href="https://fonts.googleapis.com/css2?family=Arimo:wght@400;700&display=swap">
<style>
  :root {
    --page: #e4e4e2;
    --card-light: #7c807f;
    --card-mid: #6a6e6d;
    --card-dark: #565a5a;
    --slate: #3e4b53;
    --slate-light: #8fa1aa;
    --swoosh: #f2f4f4;
    --text-soft: #c9cdcc;
    --text-muted: #a9aeae;
    --photo-top: #8a8f92;
    --photo-bottom: #2a2c2e;
  }
  * { box-sizing: border-box; margin: 0; padding: 0; }
  html, body {
    width: 1200px;
    height: 843px;
    overflow: hidden;
    background: var(--page);
    font-family: "Arimo", Arial, sans-serif;
  }
  .canvas {
    position: relative;
    width: 1200px;
    height: 843px;
  }
  .card {
    position: absolute;
    top: 273px;
    width: 520px;
    height: 297px;
    overflow: hidden;
    border-radius: 4px;
    background: linear-gradient(160deg, var(--card-light) 0%, var(--card-mid) 55%, var(--card-dark) 100%);
    box-shadow: 0 6px 18px rgba(0,0,0,.22);
  }
  .card--back { left: 60px; }
  .card--front { left: 620px; }

  /* back side */
  .back-text {
    position: absolute;
    left: 0; right: 0;
    top: 138px;
    text-align: center;
  }
  .back-web {
    font-size: 15px;
    color: var(--text-soft);
    letter-spacing: .3px;
  }
  .back-tagline {
    margin-top: 5px;
    font-size: 10px;
    color: var(--text-muted);
    letter-spacing: .4px;
  }

  /* front side */
  .front-shapes {
    position: absolute;
    inset: 0;
    width: 520px;
    height: 297px;
  }
  .identity {
    position: absolute;
    left: 46px;
    top: 44px;
  }
  .name {
    font-size: 17px;
    color: var(--text-soft);
    font-weight: 400;
  }
  .role {
    margin-top: 3px;
    font-size: 11px;
    color: var(--text-muted);
  }
  .contact {
    position: absolute;
    left: 46px;
    top: 106px;
    list-style: none;
    font-size: 12.5px;
    color: var(--text-soft);
    line-height: 17px;
  }
  .contact .phone { font-size: 15px; margin-bottom: 2px; }
  .portrait {
    position: absolute;
    right: 0;
    bottom: 0;
    width: 188px;
    height: 205px;
    background: linear-gradient(180deg, var(--photo-top) 0%, #5b5f62 45%, var(--photo-bottom) 100%);
  }
</style>
</head>
<body>
<main class="canvas">

  <section class="card card--back" aria-label="Card back">
    <div class="back-text">
      <p class="back-web">www.ostranderthrillers.example</p>
      <p class="back-tagline">Writing legal thrillers and mysteries</p>
    </div>
  </section>

  <section class="card card--front" aria-label="Card front">
    <svg class="front-shapes" viewBox="0 0 520 297" aria-hidden="true">
      <defs>
        <linearGradient id="swooshFade" x1="0" y1="0" x2="1" y2="0">
          <stop offset="0" stop-color="#f2f4f4" stop-opacity=".15"/>
          <stop offset=".5" stop-color="#f2f4f4" stop-opacity=".95"/>
          <stop offset="1" stop-color="#f2f4f4"/>
        </linearGradient>
        <linearGradient id="slateBand" x1="0" y1="0" x2="1" y2="0">
          <stop offset="0" stop-color="#3e4b53"/>
          <stop offset="1" stop-color="#4d5b63"/>
        </linearGradient>
      </defs>
      <!-- top swoosh -->
      <path d="M0 0 H520 V40 C420 6 260 2 120 22 C70 28 30 20 0 8 Z" fill="url(#swooshFade)"/>
      <path d="M130 28 C260 10 420 14 520 48 V56 C420 24 260 20 130 28 Z" fill="#ffffff" opacity=".55"/>
      <!-- bottom band -->
      <path d="M0 232 C120 250 260 228 380 196 C430 182 480 168 520 160 V297 H0 Z" fill="url(#slateBand)"/>
      <path d="M0 226 C120 244 260 222 380 190 C430 176 480 162 520 154 V162 C480 170 430 184 380 198 C260 230 120 252 0 234 Z" fill="#8fa1aa" opacity=".7"/>
    </svg>

    <div class="identity">
      <h1 class="name">Paul Ostrander</h1>
      <p class="role">Writer</p>
    </div>

    <ul class="contact">
      <li class="phone">0064 27 5139427</li>
      <li class="email">paulbostrander@mailbox.example</li>
      <li class="web">www.ostranderthrillers.example</li>
    </ul>

    <div class="portrait" role="img" aria-label="Portrait photograph of the author in a dark jacket and white shirt"></div>
  </section>

</main>
</body>
</html>
```